Coaching company requires a Bi-Fold Services Brochure

**Please also read attached design brief***

As part of our expanding sales role for our Professional Development Company, we need a Bi-Fold services brochure that offers our clients some further information about our specific services.

This services brochure will be the document that our clients will receive after our initial contact with them so the overall design of this document will play an instrumental part in our securing of ongoing work.

We have prepared a design brief for designers that want to undertake this task and this document should help to clarify any missing information from this online brief. Any designer who is interested in submitting a design should also refer to this attached document to get the full scope of the works required.

Regular email correspondence will also be available to clarify any questions that the design may have

*** Please also note that the finished design will need to be submitted in a PSD format to allow for editing in Photoshop CS6

Target Market(s)

Our target market is Business to Business. We are specifically targeting small, medium and large businesses who are looking to invest in Professional Development for their business and their staff.
The areas of major focus are 1 on 1 coaching of leaders, executives & business owners and group facilitation sessions with their staff.

Industry/Entity Type

Business Service

Font styles to use
Sans Serif

Requirements
Must have
• - Design needs to be an A4 Bi-Fold layout so should suit an A3 sheet of paper (297mm x 420mm)
• - Include our corporate color scheme
• - Finished design must be in PSD format or format that can be edited in Photshop CS6
• - Appealing to small, medium and large businesses (universal appeal)
• - The project must be in CMYK Colour and no less than 300 pixel resolution
Nice to have
• - Our logo incorporated into the front page
• - We would like the images used in this brochure to be happy and vibrant (i.e. smiling faces and energetic etc.)

```html
<!DOCTYPE html>
<html lang="en">
<head>
<meta charset="utf-8">
<title>Services Brochure – Our Services</title>
<link rel="stylesheet" href="https://fonts.googleapis.com/css2?family=Oswald:wght@500;600;700&family=Arimo:wght@400&display=swap">
<style>
  :root {
    --brand-blue: #1f9ad6;
    --brand-grey: #68696c;
    --brand-red: #e3261c;
    --page-bg: #f2f2f4;
    --canvas-bg: #ffffff;
    --ink: #1e1e1e;
    --photo-light: #e9e6e2;
    --photo-mid: #b9a58f;
    --photo-dark: #7d6a58;
  }
  * { box-sizing: border-box; margin: 0; padding: 0; }
  html, body {
    width: 1008px; height: 1200px; overflow: hidden;
    background: var(--canvas-bg);
  }
  .page {
    position: absolute; left: 86px; top: 10px;
    width: 835px; height: 1180px;
    background: var(--page-bg);
    font-family: "Arimo", Arial, sans-serif;
    color: var(--ink);
  }
  .page-title {
    position: absolute; left: 56px; top: 44px;
    font-family: "Oswald", sans-serif; font-weight: 700;
    font-size: 42px; letter-spacing: -0.5px; line-height: 1;
    color: var(--brand-blue); text-transform: uppercase;
  }
  .service-column { position: absolute; top: 134px; width: 232px; }
  .service-column--coaching { left: 58px; }
  .service-column--facilitation { left: 303px; }
  .service-column--courses { left: 548px; }
  .service-header {
    height: 49px; display: flex; align-items: center; justify-content: center;
    font-family: "Oswald", sans-serif; font-weight: 600; font-size: 21px;
    color: #fff; text-transform: uppercase; letter-spacing: 0.2px;
    background: var(--brand-blue);
  }
  .service-column--facilitation .service-header { background: var(--brand-grey); }
  .service-body {
    padding: 26px 14px 0; text-align: center;
    font-size: 14.2px; line-height: 18.2px;
  }
  .service-subhead {
    font-family: "Oswald", sans-serif; font-weight: 500; font-size: 15.5px;
    line-height: 20px; color: var(--brand-blue); margin-bottom: 10px;
  }
  .service-subhead .accent { color: var(--brand-red); }
  .service-text + .service-subhead { margin-top: 26px; }
  .service-text + .service-subhead.extra-gap { margin-top: 36px; }
  .team-photo {
    position: absolute; left: 294px; top: 636px; width: 483px; height: 484px;
    background:
      linear-gradient(90deg, var(--page-bg) 0%, rgba(242,242,244,0) 28%),
      linear-gradient(180deg, var(--page-bg) 0%, rgba(242,242,244,0) 22%),
      linear-gradient(180deg, var(--photo-light) 0%, #d8d2ca 55%, var(--photo-mid) 82%, var(--photo-dark) 100%);
  }
  .page-footer {
    position: absolute; right: 55px; top: 1133px;
    display: flex; align-items: center; gap: 6px;
    font-family: "Oswald", sans-serif; font-weight: 500; font-size: 14px;
    color: var(--ink); text-transform: uppercase; letter-spacing: -0.2px;
  }
  .page-footer .divider { margin: 0 3px; }
  .footer-mark { width: 28px; height: 28px; }
</style>
</head>
<body>
  <main class="page">
    <h1 class="page-title">Our Services</h1>

    <section class="service-column service-column--coaching">
      <h2 class="service-header">Coaching</h2>
      <div class="service-body">
        <h3 class="service-subhead">“People Centric”<br>Leadership <span class="accent">Coaching</span>:</h3>
        <p class="service-text">Our “People Centric” Leader-ship Coaching Service is specifically designed to assist new, existing and emerging leaders to identify and harness their true leadership potential to create a resonating people based culture throughout their business. This also includes obtaining their immediate and long term leadership goals, as well as their most important personal development needs, all within the shortest time possible.</p>
        <h3 class="service-subhead">Executive <span class="accent">Coaching</span>:</h3>
        <p class="service-text">Our Executive Coaching sessions provide experienced business owners, managing directors and senior executives with personalised, one on one, self-propelled development that aligns thoughts, feelings and actions to gain instant clarity and traction and produce results.</p>
        <h3 class="service-subhead extra-gap">Small Business <span class="accent">Coaching</span>:</h3>
        <p class="service-text">Our Small Business Coaching provides business owners and managers with self-directed strategic and business development tools and actions designed to drive their business forward. From the creation of a Vision, all the way through to strategic develop plans, we can help you paint that clear picture and follow through to achieve your desired outcomes.</p>
      </div>
    </section>

    <section class="service-column service-column--facilitation">
      <h2 class="service-header">Group Facilitation</h2>
      <div class="service-body">
        <p class="service-text">Our Group Facilitation Service utilises thorough planning, skilful guidance, and expert group management techniques to provide your team with clear “outside the box” thinking, enthusiastic participation and full “buy in” to reach their desired outcomes. So if you are looking for expert guidance to find those elusive business solutions, drive your business and operational concepts forward and combine the skills, knowledge and motivation of your teams, then our Group Facilitation Service will suit your needs!</p>
      </div>
    </section>

    <section class="service-column service-column--courses">
      <h2 class="service-header">Customised Courses</h2>
      <div class="service-body">
        <p class="service-text">Unlike the traditional “one boot fits all” approach to training, we work closely with your business to identify skills gap and create courses that will meet your immediate training needs. Through the creation and delivery of tailor-made training content, we can ensure that your business is receiving the right training with the right outcomes and guaranteed to bridge those immediate knowledge gaps.</p>
      </div>
    </section>

    <div class="team-photo" role="img" aria-label="Photo of three smiling colleagues gathered around a laptop at a wooden table in a bright office"></div>

    <footer class="page-footer">
      <span class="page-number">03</span><span class="divider">|</span><span>Services Brochure</span>
      <svg class="footer-mark" viewBox="0 0 28 28" aria-hidden="true">
        <circle cx="14" cy="14" r="5" fill="var(--brand-blue)"/>
      </svg>
    </footer>
  </main>
</body>
</html>
```